Multi Academy Trust needs to shout about our vision by turning our words into something that can ...

Our vision is something we want to shout about and share through multiple media avenues to a range of stakeholders including parents, staff, pupils, other school trusts, Council for Civic Standards and suppliers. We want an eye-catching design that stands out from the crowd but incorporates our current brand (and logo)

```html
<!DOCTYPE html>
<html lang="en">
<head>
<meta charset="utf-8">
<title>Northfield Learning Partnership – Our Vision</title>
<link href="https://fonts.googleapis.com/css2?family=Barlow:wght@400;600&family=Saira:wght@700;800&display=swap" rel="stylesheet">
<style>
  :root {
    --paper: #ffffff;
    --ink: #3a3a3a;
    --brand-grey: #6d6e70;
    --brand-blue: #1f8fd0;
    --panel-blue: #9fd3ee;
    --night-deep: #0a1f4e;
    --night-mid: #1c4b95;
    --glow: #cfe2f7;
    --headline: #ffffff;
  }
  * { margin: 0; padding: 0; box-sizing: border-box; }
  html, body {
    width: 1155px;
    height: 1200px;
    overflow: hidden;
    background: var(--paper);
  }
  .poster {
    position: relative;
    width: 1155px;
    height: 1200px;
    background: var(--paper);
    font-family: "Barlow", Arial, sans-serif;
    color: var(--ink);
  }
  .brand {
    position: absolute;
    top: 78px;
    right: 50px;
    display: flex;
    align-items: center;
    gap: 12px;
  }
  .brand__dot {
    width: 20px;
    height: 20px;
    border-radius: 50%;
    background: var(--brand-blue);
  }
  .brand__name {
    font-family: "Barlow", Arial, sans-serif;
    font-weight: 400;
    font-size: 26px;
    line-height: 30px;
    color: var(--brand-grey);
    white-space: nowrap;
  }
  .hero {
    position: absolute;
    top: 226px;
    left: 42px;
    width: 1064px;
    height: 666px;
    overflow: hidden;
  }
  .hero__image {
    position: absolute;
    inset: 0;
    background:
      radial-gradient(circle at 32% 45%, var(--glow) 0%, rgba(120,170,230,0.55) 16%, rgba(28,75,149,0) 38%),
      radial-gradient(ellipse at 30% 98%, rgba(230,235,240,0.85) 0%, rgba(120,140,170,0.35) 18%, rgba(10,31,78,0) 40%),
      linear-gradient(180deg, var(--night-mid) 0%, #173f80 45%, var(--night-deep) 100%);
  }
  .hero__headline {
    position: absolute;
    left: 460px;
    top: 573px;
    font-family: "Saira", Arial, sans-serif;
    font-weight: 800;
    font-size: 37px;
    line-height: 40px;
    color: var(--headline);
    letter-spacing: 0.3px;
  }
  .vision {
    position: absolute;
    top: 905px;
    left: 42px;
    width: 1064px;
    height: 270px;
    background: var(--panel-blue);
  }
  .vision__content {
    position: absolute;
    left: 460px;
    top: 22px;
    width: 580px;
    font-size: 16px;
    line-height: 20px;
  }
  .vision__heading {
    font-family: "Saira", Arial, sans-serif;
    font-weight: 700;
    font-size: 15px;
    margin-bottom: 20px;
  }
  .vision__list { list-style: none; }
  .vision__list li {
    padding-left: 20px;
    text-indent: -20px;
  }
</style>
</head>
<body>
  <main class="poster">
    <header class="brand">
      <span class="brand__dot"></span>
      <span class="brand__name">Northfield Learning Partnership</span>
    </header>

    <section class="hero">
      <div class="hero__image" role="img" aria-label="Silhouetted hands reaching towards a glowing globe wrapped in a network of connected points against a deep blue sky"></div>
      <h1 class="hero__headline">What does this look like<br>across our trust?</h1>
    </section>

    <section class="vision">
      <div class="vision__content">
        <h2 class="vision__heading">Education</h2>
        <p class="vision__intro">We are:</p>
        <ol class="vision__list">
          <li>1. Ruthlessly ambitious for all who learn and work with us</li>
          <li>2. Unwaveringly inclusive – determined on eradicating barriers<br>to educational success</li>
          <li>3. Committed to excellent teaching</li>
          <li>4. Determined upon academic excellence for all in our communities</li>
          <li>5. Compassionate, ethical and caring advocates for all in our<br>communities</li>
          <li>6. Outwardly facing and globally conscious</li>
        </ol>
      </div>
    </section>
  </main>
</body>
</html>
```